New Property management company business cards

Looking for a new business card, to reflect new younger ownership
Card should be clean, simple and professional but with a modern layout that is conveys our new logo and business model

Key aspects of the business:

Property Management
Facility Maintenance
Project Management
Tenant Improvements

Mailing Address:
PO BOX 7186
Brindale CA, 95012

Phone: 209-614-8837
Direct: 209-614-8831

Doyle Farrant
President

Target Market(s)

Commercial property owners

Industry/Entity Type

Real Estate property management

Contact Information for Business Card

Open to all designs but lean toward vertical layouts

Requirements
Must have
• Logo and space to customize name and contact info

```html
<!DOCTYPE html>
<html lang="en">
<head>
<meta charset="utf-8">
<title>Valleron Business Card</title>
<link rel="stylesheet" href="https://fonts.googleapis.com/css2?family=Heebo:wght@400;500;700&display=swap">
<style>
  :root {
    --backdrop: #e4e4e4;
    --ink-dark: #31313d;
    --paper: #f4f4f4;
    --teal: #1aa6a0;
    --text-dark: #2f2f38;
    --white: #ffffff;
  }
  * { margin: 0; padding: 0; box-sizing: border-box; }
  html, body {
    width: 1200px; height: 960px; overflow: hidden;
    background: var(--backdrop);
    font-family: "Heebo", Arial, sans-serif;
  }
  .stage { position: relative; width: 1200px; height: 960px; }
  .card {
    position: absolute; top: 178px;
    width: 345px; height: 604px; overflow: hidden;
  }
  .card--front { left: 229px; background: var(--ink-dark); }
  .card--back { left: 627px; background: var(--paper); }

  .brand {
    position: absolute; top: 266px; left: 0; width: 100%;
    display: flex; justify-content: center; align-items: center; gap: 10px;
  }
  .brand__square { width: 16px; height: 16px; background: var(--white); }
  .brand__name {
    color: var(--white); font-weight: 500; font-size: 32px; letter-spacing: 5px;
  }
  .services {
    position: absolute; top: 438px; left: 0; width: 100%;
    list-style: none; text-align: center;
    color: var(--white); font-size: 19.3px; line-height: 26.3px;
  }

  .back-top { position: absolute; top: 0; left: 0; }
  .person {
    position: absolute; top: 295px; left: 0; width: 100%; text-align: center;
  }
  .person__name {
    color: var(--teal); font-weight: 700; font-size: 23px; letter-spacing: 0.5px; line-height: 27px;
  }
  .person__title { color: var(--text-dark); font-size: 18.5px; line-height: 24px; }
  .divider { position: absolute; left: 79px; }
  .contact {
    position: absolute; left: 0; width: 100%; text-align: center;
    color: var(--text-dark); font-size: 19px; line-height: 23px; font-style: normal;
  }
  .contact--address { top: 405px; }
  .contact--phone { top: 497px; }
  .contact__label { color: var(--teal); }
</style>
</head>
<body>
<main class="stage">
  <section class="card card--front">
    <div class="brand">
      <span class="brand__square"></span>
      <span class="brand__name">VALLERON</span>
    </div>
    <ul class="services">
      <li>Property Management</li>
      <li>Facility Maintenance</li>
      <li>Project Management</li>
      <li>Tenant Improvements</li>
    </ul>
  </section>

  <section class="card card--back">
    <svg class="back-top" width="345" height="240" viewBox="0 0 345 240">
      <polygon points="0,0 345,0 345,234 172,62 0,234" fill="var(--ink-dark)"/>
    </svg>

    <div class="person">
      <p class="person__name">DOYLE FARRANT</p>
      <p class="person__title">President</p>
    </div>

    <svg class="divider" style="top:380px" width="188" height="22" viewBox="0 0 188 22">
      <line x1="0" y1="12" x2="82" y2="12" stroke="var(--teal)" stroke-width="1.3"/>
      <line x1="106" y1="12" x2="188" y2="12" stroke="var(--teal)" stroke-width="1.3"/>
      <path d="M94 19 C90 14 88 11 88 8.5 A6 6 0 0 1 100 8.5 C100 11 98 14 94 19 Z" fill="none" stroke="var(--teal)" stroke-width="1.3"/>
      <circle cx="94" cy="8.5" r="2" fill="none" stroke="var(--teal)" stroke-width="1.2"/>
    </svg>
    <address class="contact contact--address">
      <p>PO BOX 7186</p>
      <p>Brindale CA, 95012</p>
    </address>

    <svg class="divider" style="top:472px" width="188" height="20" viewBox="0 0 188 20">
      <line x1="0" y1="10" x2="82" y2="10" stroke="var(--teal)" stroke-width="1.3"/>
      <line x1="106" y1="10" x2="188" y2="10" stroke="var(--teal)" stroke-width="1.3"/>
      <path d="M89 5 L91.5 3 L94 7 L92.5 8.5 C93.5 11 95 12.5 97 13.5 L98.5 12 L102 14.5 L100 17 C94 16.5 89.5 12 89 5 Z" fill="none" stroke="var(--teal)" stroke-width="1.2" stroke-linejoin="round"/>
    </svg>
    <div class="contact contact--phone">
      <p><span class="contact__label">Office:</span> 209-614-8837</p>
      <p><span class="contact__label">Direct:</span> 209-614-8831</p>
    </div>
  </section>
</main>
</body>
</html>
```